Business Card Design Project

The business card is for an educational company that provides personalised tuition to students.

The company logo is in orange and blue (as provided) and should be included in the name card design

The philosophy of the company is to make learning a comfortable experience for student as such design of the namecard should look fresh and has a bit of the 'wow' factor. Some of the namecard design that appeals to me are as uploaded under Sample Design.

The particulars that need to be provided are:
(1): Company Name (Quillmont Education)
(1): Name
(2): Educational qualifications which will appear below name
(3): Mobile number
(4): Email address
(5): Website

Industry/Entity Type

Business

Requirements
Must have
• (1): Company Logo

(2): The card background should preferably be coloured both for the front side and back.

(3): The choice of font is important as part of the selection consideration. There is no preferred font that I have selected, designer is free to choose the font that will complement their design.

```html
<!DOCTYPE html>
<html lang="en">
<head>
<meta charset="utf-8">
<title>Quillmont Education – Business Card</title>
<link href="https://fonts.googleapis.com/css2?family=Libre+Baskerville:wght@400;700&family=Open+Sans:wght@400&display=swap" rel="stylesheet">
<style>
  :root {
    --backdrop: #3b3b3d;
    --card-white: #ffffff;
    --ink-grey: #58585a;
    --brand-blue: #2d78b6;
    --brand-blue-light: #3aa0d8;
    --brand-blue-deep: #245e97;
    --brand-orange: #f39a2a;
    --brand-orange-deep: #e8501e;
    --text-white: #ffffff;
    --serif: "Libre Baskerville", Georgia, serif;
    --sans: "Open Sans", Arial, sans-serif;
  }
  * { margin: 0; padding: 0; box-sizing: border-box; }
  html, body { width: 1200px; height: 900px; overflow: hidden; }
  body { background: var(--backdrop); position: relative; }

  .card {
    position: absolute;
    top: 308px;
    width: 514px;
    height: 284px;
    border-radius: 14px;
    overflow: hidden;
    box-shadow: 0 3px 8px rgba(0,0,0,0.35);
  }
  .card--front { left: 73px; background: var(--card-white); }
  .card--back { left: 616px; }

  /* Front */
  .front-brand {
    position: absolute;
    left: 45px;
    top: 100px;
    display: flex;
    align-items: center;
    gap: 12px;
  }
  .brand-square {
    width: 82px; height: 82px;
    border-radius: 10px;
    background: var(--brand-orange);
    flex: none;
  }
  .brand-name {
    font-family: var(--serif);
    font-weight: 400;
    font-size: 34px;
    line-height: 1.1;
    color: var(--ink-grey);
  }

  /* Back */
  .back-bg { position: absolute; inset: 0; width: 100%; height: 100%; }
  .back-brand {
    position: absolute;
    left: 28px; top: 24px;
    font-family: var(--serif);
    font-size: 26px;
    line-height: 1.15;
    color: var(--text-white);
  }
  .holder {
    position: absolute;
    right: 28px; top: 122px;
    text-align: right;
    color: var(--text-white);
  }
  .holder-name { font-family: var(--serif); font-weight: 700; font-size: 18px; }
  .holder-title { font-family: var(--serif); font-size: 13px; margin-top: 3px; }
  .contacts {
    position: absolute;
    right: 28px; top: 214px;
    list-style: none;
    font-family: var(--sans);
    font-size: 12px;
    line-height: 16px;
    color: var(--text-white);
    text-align: right;
  }
  .contacts li { display: flex; justify-content: flex-end; align-items: center; gap: 5px; }
  .contacts svg { width: 10px; height: 10px; flex: none; }
</style>
</head>
<body>
  <section class="card card--front" aria-label="Card front">
    <div class="front-brand">
      <span class="brand-square" aria-hidden="true"></span>
      <p class="brand-name">Quillmont<br>Education</p>
    </div>
  </section>

  <section class="card card--back" aria-label="Card back">
    <svg class="back-bg" viewBox="0 0 514 284" preserveAspectRatio="none" aria-hidden="true">
      <defs>
        <radialGradient id="blueField" cx="0.35" cy="0.35" r="0.8">
          <stop offset="0" stop-color="var(--brand-blue-light)"/>
          <stop offset="1" stop-color="var(--brand-blue-deep)"/>
        </radialGradient>
        <linearGradient id="orangeField" x1="0" y1="0" x2="1" y2="0">
          <stop offset="0.3" stop-color="var(--brand-orange)"/>
          <stop offset="1" stop-color="var(--brand-orange-deep)"/>
        </linearGradient>
      </defs>
      <rect width="514" height="284" fill="url(#blueField)"/>
      <path d="M373,0 C250,40 150,150 117,284 L514,284 L514,0 Z" fill="url(#orangeField)"/>
    </svg>

    <p class="back-brand">Quillmont<br>Education</p>

    <div class="holder">
      <p class="holder-name">Daniel Harrow</p>
      <p class="holder-title">dr. of philosophy</p>
    </div>

    <ul class="contacts">
      <li>555 014 27 63
        <svg viewBox="0 0 10 10" aria-hidden="true"><rect x="2.5" y="0.5" width="5" height="9" rx="1" fill="none" stroke="#fff"/><rect x="3.5" y="1.8" width="3" height="5" fill="#fff"/></svg>
      </li>
      <li>info@quillmonteducation.com
        <svg viewBox="0 0 10 10" aria-hidden="true"><rect x="0.5" y="2" width="9" height="6" fill="#fff"/><path d="M0.5,2 L5,5.5 L9.5,2" fill="none" stroke="#e8501e" stroke-width="0.8"/></svg>
      </li>
      <li>www.quillmonteducation.com
        <svg viewBox="0 0 10 10" aria-hidden="true"><circle cx="5" cy="5" r="4.5" fill="#fff"/><path d="M0.5,5 H9.5 M5,0.5 V9.5 M5,0.5 C2.5,3 2.5,7 5,9.5 M5,0.5 C7.5,3 7.5,7 5,9.5" fill="none" stroke="#e8501e" stroke-width="0.6"/></svg>
      </li>
    </ul>
  </section>
</body>
</html>
```